BrightOak Cards, letterhead, and envelopes
BrightOak Technologies and Rx
BrightOak Cards, letterhead, and envelopes - Information Technology
Creative Brief
Use same font as used in my logo
or as you see fit
Professional
Thomas R. Perlavic
President, CEO
4817 S. Harlan Crest Avenue Suite 300
tperlavic@BrightOakTech.example
www.BrightOakTech.example
On the front of the business card please use the BrightOak Technologies logo, the BrightOakTech.example website, and integrate the i graphic with a shadow effect. On the back of the business card, please use the square logo (i with the Rx), the i graphic with the shadow effect and list the BrightOakRx.example website.

```html
<!DOCTYPE html>
<html lang="en">
<head>
<meta charset="utf-8">
<title>BrightOak Stationery</title>
<link rel="stylesheet" href="https://fonts.googleapis.com/css2?family=Open+Sans:wght@400;600;700&display=swap">
<style>
:root{
  --bg:#8d8f92;
  --paper:#ffffff;
  --ink:#4a4f55;
  --muted:#8a9096;
  --brand:#1d6fa8;
  --deep:#0d4f86;
  --bright:#2f8fd0;
  --line:#b9bec3;
  --ghost:#eef1ec;
}
*{box-sizing:border-box;margin:0;padding:0}
html,body{width:1200px;height:564px;overflow:hidden}
body{background:var(--bg);font-family:"Open Sans",Arial,sans-serif;color:var(--ink);position:relative}
.sheet{position:absolute;background:var(--paper);box-shadow:0 2px 6px rgba(0,0,0,.25);overflow:hidden}
.letter{top:24px;width:360px;height:516px}
.fax-sheet{left:24px}
.plain-sheet{left:403px}
.wordmark{color:var(--brand);font-weight:700;letter-spacing:-.5px;line-height:1;display:flex;align-items:center;gap:5px}
.wordmark .dot{width:8px;height:8px;border-radius:50%;background:var(--bright)}
.letter .wordmark{position:absolute;top:26px;left:0;right:0;justify-content:center;font-size:26px}
.letter .tagline{position:absolute;top:56px;left:0;right:0;text-align:center;font-size:6px;color:var(--muted)}
.fax-label{position:absolute;top:58px;right:20px;font-size:9px;font-weight:700;color:var(--ink)}
.fax-table{position:absolute;top:72px;left:18px;width:324px;border-collapse:collapse;font-size:6px}
.fax-table td{border:1px solid var(--line);height:18px;padding:0 4px}
.fax-table td.k{width:42px;color:var(--muted)}
.checks{position:absolute;top:158px;left:18px;right:18px;display:flex;justify-content:space-between;font-size:6px;color:var(--muted)}
.checks span::before{content:"";display:inline-block;width:6px;height:6px;border:1px solid var(--line);margin-right:3px;vertical-align:-1px}
.ghost-mark{position:absolute;right:-20px;top:210px;width:280px;height:290px;border-radius:50%;background:radial-gradient(circle at 55% 45%,var(--ghost) 0%,#f6f8f5 55%,rgba(255,255,255,0) 72%)}
.footer{position:absolute;bottom:14px;left:0;right:0;text-align:center;font-size:5px;color:var(--muted)}
.card{top:29px;width:154px;height:84px}
.card-front{left:787px}
.card-back{left:955px;background:linear-gradient(135deg,var(--bright),var(--deep))}
.card-front svg{position:absolute;left:0;top:0}
.card-front .wordmark{position:absolute;top:8px;left:40px;font-size:12px}
.card-front .contact{position:absolute;left:40px;top:28px;font-size:4px;line-height:1.5;color:var(--muted)}
.card-front .person{position:absolute;right:8px;top:50px;text-align:right;font-size:4.5px;line-height:1.4}
.card-front .person b{color:var(--brand);font-size:5px}
.card-back .badge{position:absolute;left:66px;top:18px;width:22px;height:22px;background:#fff;opacity:.9}
.card-back .site{position:absolute;left:0;right:0;top:48px;text-align:center;font-size:4.5px;color:#fff;letter-spacing:.5px}
.envelope{left:787px;width:389px}
.env-front{top:137px;height:182px}
.env-front .wordmark{position:absolute;top:14px;left:18px;font-size:22px}
.env-front .return{position:absolute;top:44px;left:18px;font-size:4.5px;line-height:1.5;color:var(--muted)}
.env-front .ghost-mark{right:-60px;top:20px;width:220px;height:220px}
.env-back{top:343px;height:173px}
.env-back svg{position:absolute;left:0;top:0}
.env-back .badge{position:absolute;left:184px;top:62px;width:20px;height:20px;background:#fff}
.env-back .site{position:absolute;left:0;right:0;top:88px;text-align:center;font-size:4.5px;color:#fff;letter-spacing:.5px}
</style>
</head>
<body>

<section class="sheet letter fax-sheet">
  <div class="wordmark"><span class="dot"></span>BrightOak</div>
  <div class="tagline">Technologies and Rx</div>
  <div class="fax-label">FAX</div>
  <table class="fax-table">
    <tr><td class="k">To:</td><td></td><td class="k">From:</td><td></td></tr>
    <tr><td class="k">Fax:</td><td></td><td class="k">Pages:</td><td></td></tr>
    <tr><td class="k">Phone:</td><td></td><td class="k">Date:</td><td></td></tr>
    <tr><td class="k">Re:</td><td></td><td class="k">CC:</td><td></td></tr>
  </table>
  <div class="checks"><span>Urgent</span><span>For Review</span><span>Please Comment</span><span>Please Reply</span><span>Please Recycle</span></div>
  <div class="ghost-mark" role="img" aria-label="Faint brand figure watermark"></div>
  <div class="footer">4817 S. Harlan Crest Avenue Suite 300 · Tel 555-0142 · tperlavic@BrightOakTech.example · www.BrightOakTech.example</div>
</section>

<section class="sheet letter plain-sheet">
  <div class="wordmark"><span class="dot"></span>BrightOak</div>
  <div class="tagline">Technologies and Rx</div>
  <div class="ghost-mark" role="img" aria-label="Faint brand figure watermark"></div>
  <div class="footer">4817 S. Harlan Crest Avenue Suite 300 · Tel 555-0142 · tperlavic@BrightOakTech.example · www.BrightOakTech.example</div>
</section>

<section class="sheet card card-front">
  <svg width="154" height="84" viewBox="0 0 154 84" aria-hidden="true">
    <defs><linearGradient id="swoosh" x1="0" y1="0" x2="1" y2="1"><stop offset="0" stop-color="#2f8fd0"/><stop offset="1" stop-color="#0d4f86"/></linearGradient></defs>
    <path d="M0 0H30C18 20 16 60 34 84H0Z" fill="url(#swoosh)"/>
  </svg>
  <div class="wordmark">BrightOak</div>
  <div class="contact">4817 S. Harlan Crest Avenue Suite 300<br>Tel 555-0142</div>
  <div class="person"><b>Thomas R. Perlavic</b><br>President, CEO<br>tperlavic@BrightOakTech.example<br>www.BrightOakTech.example</div>
</section>

<section class="sheet card card-back">
  <div class="badge"></div>
  <div class="site">BrightOakRx.example</div>
</section>

<section class="sheet envelope env-front">
  <div class="wordmark"><span class="dot"></span>BrightOak</div>
  <div class="return">BrightOak Technologies<br>4817 S. Harlan Crest Avenue Suite 300</div>
  <div class="ghost-mark" role="img" aria-label="Faint brand figure watermark"></div>
</section>

<section class="sheet envelope env-back">
  <svg width="389" height="173" viewBox="0 0 389 173" aria-hidden="true">
    <defs><linearGradient id="flap" x1="0" y1="0" x2="0" y2="1"><stop offset="0" stop-color="#0d4f86"/><stop offset="1" stop-color="#2f8fd0"/></linearGradient></defs>
    <path d="M0 0H389V22C320 60 250 100 194 112C138 100 68 60 0 22Z" fill="url(#flap)"/>
  </svg>
  <div class="badge"></div>
  <div class="site">BrightOakRx.example</div>
</section>

</body>
</html>
```